Redesign a Shopify Banner for a spiritual streetwear brand

Redesign Shopify banner for a brand called Vorel Studios we are a spiritually inspired streetwear brand that makes lots of designs with spiritual symbols and space aesthetics like stars. I would like the banner redesigned with the star print I included in this file in the background of the banner with our logo and tag line "spiritually inspired streetwear". you can choose a new font for the banner that could be more aesthetically pleasing. you could also included other alchemical and occult or witchy symbols on the banner along with the stars. or just create the banner with the stars I included in this file. Looking forward to see your work! Thank You.
our website right now is vorel-studios.example

```html
<!DOCTYPE html>
<html lang="en">
<head>
<meta charset="utf-8">
<title>Vorel Studios – Banner Concepts</title>
<link rel="stylesheet" href="https://fonts.googleapis.com/css2?family=Quicksand:wght@500;700&family=Comic+Neue:wght@400;700&display=swap">
<style>
  :root {
    --page-bg: #c6c6c6;
    --night-black: #000000;
    --charcoal: #1e1e1f;
    --ink: #1b1b1d;
    --star-white: #ffffff;
    --star-dim: #d9d9d9;
    --frame-line: #f2f2f2;
    --amethyst: #a865c0;
    --line-art: rgba(120, 135, 135, 0.22);
    --panel-shadow: 0 8px 22px rgba(0, 0, 0, 0.35);
  }
  * { margin: 0; padding: 0; box-sizing: border-box; }
  html, body {
    width: 814px;
    height: 1200px;
    overflow: hidden;
    background: var(--page-bg);
  }
  .sheet { position: relative; width: 814px; height: 1200px; }
  .banner {
    position: absolute;
    left: 55px;
    width: 704px;
    height: 326px;
    box-shadow: var(--panel-shadow);
    overflow: hidden;
    color: var(--star-white);
  }
  .banner--starfield { top: 56px; background: var(--night-black); }
  .banner--framed { top: 437px; background: var(--charcoal); }
  .banner--occult { top: 817px; background: var(--ink); }

  .banner__texture {
    position: absolute;
    inset: 0;
    background: radial-gradient(ellipse at 30% 40%, #262627 0%, #1c1c1d 60%, #202021 100%);
  }
  .banner__stars { position: absolute; inset: 0; width: 704px; height: 326px; }

  .occult-border {
    position: absolute;
    inset: 0;
    background:
      radial-gradient(ellipse 62% 44% at 50% 50%, var(--ink) 60%, transparent 100%),
      linear-gradient(135deg, var(--line-art), rgba(90, 105, 105, 0.12) 50%, var(--line-art));
  }

  .brand-name {
    position: absolute;
    left: 0;
    right: 0;
    text-align: center;
    font-weight: 700;
    color: var(--star-white);
    letter-spacing: 1px;
    white-space: nowrap;
  }
  .tagline {
    position: absolute;
    left: 0;
    right: 0;
    text-align: center;
    white-space: nowrap;
  }

  /* Banner 1 */
  .banner--starfield .brand-name {
    top: 133px;
    font-family: "Quicksand", sans-serif;
    font-size: 52px;
    line-height: 60px;
    margin-top: -30px;
  }
  .banner--starfield .tagline {
    top: 256px;
    font-family: "Quicksand", sans-serif;
    font-weight: 500;
    font-size: 23px;
    line-height: 28px;
  }

  /* Banner 2 */
  .tag-frame {
    position: absolute;
    left: 153px;
    top: 111px;
    width: 397px;
    height: 148px;
    border: 1px solid var(--frame-line);
    border-radius: 12px;
  }
  .banner--framed .brand-name {
    top: 86px;
    left: 244px;
    right: 244px;
    font-family: "Comic Neue", sans-serif;
    font-size: 38px;
    line-height: 50px;
    background: var(--charcoal);
  }
  .banner--framed .tagline {
    font-family: "Comic Neue", sans-serif;
    line-height: 32px;
  }
  .tagline__lead { top: 171px; font-weight: 700; font-size: 31px; }
  .tagline__tail { top: 201px; font-weight: 400; font-size: 27px; letter-spacing: 1px; }

  /* Banner 3 */
  .banner--occult .brand-name {
    top: 118px;
    font-family: "Quicksand", sans-serif;
    font-size: 40px;
    line-height: 50px;
  }
  .banner--occult .tagline {
    top: 190px;
    font-family: "Quicksand", sans-serif;
    font-weight: 700;
    font-size: 24px;
    line-height: 30px;
    color: var(--amethyst);
  }
</style>
</head>
<body>
<main class="sheet">

  <section class="banner banner--starfield">
    <svg class="banner__stars" viewBox="0 0 704 326" role="img" aria-label="Black night sky scattered with small white stars and tiny witch hats">
      <defs>
        <pattern id="stars-fine" width="118" height="92" patternUnits="userSpaceOnUse">
          <circle cx="8" cy="12" r="0.9" fill="#fff"/>
          <circle cx="37" cy="5" r="0.7" fill="#fff"/>
          <circle cx="64" cy="27" r="1" fill="#fff"/>
          <circle cx="95" cy="14" r="0.8" fill="#fff"/>
          <circle cx="22" cy="41" r="0.7" fill="#fff"/>
          <circle cx="51" cy="56" r="0.9" fill="#fff"/>
          <circle cx="84" cy="47" r="0.7" fill="#fff"/>
          <circle cx="110" cy="63" r="1" fill="#fff"/>
          <circle cx="14" cy="74" r="0.8" fill="#fff"/>
          <circle cx="43" cy="86" r="0.7" fill="#fff"/>
          <circle cx="73" cy="79" r="0.9" fill="#fff"/>
          <circle cx="101" cy="88" r="0.6" fill="#fff"/>
        </pattern>
      </defs>
      <rect width="704" height="326" fill="url(#stars-fine)"/>
    </svg>
    <h1 class="brand-name">Vorel Studios</h1>
    <p class="tagline">SPIRITUALLY INSPIRED STREETWEAR</p>
  </section>

  <section class="banner banner--framed">
    <div class="banner__texture"></div>
    <svg class="banner__stars" viewBox="0 0 704 326" role="img" aria-label="Textured charcoal starfield with a north star, crescent moons and a weeping eye drawn in fine line">
      <defs>
        <pattern id="stars-dense" width="104" height="84" patternUnits="userSpaceOnUse">
          <circle cx="6" cy="6" r="1.3" fill="#e6e6e6"/>
          <circle cx="30" cy="3" r="1.1" fill="#e6e6e6"/>
          <circle cx="57" cy="18" r="1.4" fill="#e6e6e6"/>
          <circle cx="86" cy="9" r="1.1" fill="#e6e6e6"/>
          <circle cx="18" cy="33" r="1.2" fill="#e6e6e6"/>
          <circle cx="44" cy="44" r="1.4" fill="#e6e6e6"/>
          <circle cx="75" cy="37" r="1.1" fill="#e6e6e6"/>
          <circle cx="98" cy="52" r="1.3" fill="#e6e6e6"/>
          <circle cx="9" cy="64" r="1.1" fill="#e6e6e6"/>
          <circle cx="35" cy="76" r="1.3" fill="#e6e6e6"/>
          <circle cx="64" cy="68" r="1.2" fill="#e6e6e6"/>
          <circle cx="90" cy="80" r="1.1" fill="#e6e6e6"/>
        </pattern>
      </defs>
      <rect width="704" height="326" fill="url(#stars-dense)"/>
    </svg>
    <div class="tag-frame"></div>
    <h2 class="brand-name">Vorel Studios</h2>
    <p class="tagline tagline__lead">SPIRITUALLY INSPIRED</p>
    <p class="tagline tagline__tail">STREETWEAR</p>
  </section>

  <section class="banner banner--occult">
    <div class="occult-border" role="img" aria-label="Faint line drawings of crystals, serpents, potion bottles, an hourglass, a sun and plants framing the banner"></div>
    <svg class="banner__stars" viewBox="0 0 704 326" role="img" aria-label="Sparse white stars across the dark background">
      <defs>
        <pattern id="stars-sparse" width="140" height="108" patternUnits="userSpaceOnUse">
          <circle cx="12" cy="20" r="1.2" fill="#fff"/>
          <circle cx="58" cy="8" r="1" fill="#fff"/>
          <circle cx="104" cy="34" r="1.3" fill="#fff"/>
          <circle cx="33" cy="62" r="1" fill="#fff"/>
          <circle cx="86" cy="78" r="1.2" fill="#fff"/>
          <circle cx="126" cy="94" r="1" fill="#fff"/>
          <circle cx="6" cy="100" r="1.1" fill="#fff"/>
        </pattern>
      </defs>
      <rect width="704" height="326" fill="url(#stars-sparse)"/>
    </svg>
    <h2 class="brand-name">Vorel Studios</h2>
    <p class="tagline">Spiritually Inspired Streetwear</p>
  </section>

</main>
</body>
</html>
```